Business card design needed

Company Name: Quill Harbour

We work with boards and businesses to enhance their governance structures, board room performance
Based on the Gold Coast Australia

Industry/Entity Type

Business

Contact Information for Business Card

Melda Porrins
PO Box 572
Tallowfern Qld 4391

melda@quillharbour.com.au
0427 861593

Requirements
Nice to have
• I quite like "cogs" but am open to suggestions

```html
<!DOCTYPE html>
<html lang="en">
<head>
<meta charset="utf-8">
<title>Quill Harbour – Business Card</title>
<link rel="stylesheet" href="https://fonts.googleapis.com/css2?family=Jost:wght@400&display=swap">
<style>
  :root {
    --page-bg: #ffffff;
    --card-bg: #ffffff;
    --card-border: #bcbcbc;
    --ink: #231f20;
  }
  html, body {
    margin: 0;
    padding: 0;
    width: 1200px;
    height: 1000px;
    overflow: hidden;
    background: var(--page-bg);
  }
  .card {
    position: absolute;
    left: 216px;
    top: 288px;
    width: 762px;
    height: 433px;
    border: 3px solid var(--card-border);
    background: var(--card-bg);
    font-family: "Jost", "Futura", sans-serif;
    color: var(--ink);
  }
  .company-name {
    position: absolute;
    left: 0;
    right: 0;
    top: 160px;
    margin: 0;
    text-align: center;
    font-size: 62px;
    font-weight: 400;
    line-height: 1;
    letter-spacing: 1px;
    text-transform: uppercase;
    color: var(--ink);
  }
  .person-name {
    position: absolute;
    left: 0;
    right: 0;
    top: 262px;
    margin: 0;
    text-align: center;
    font-size: 26px;
    font-weight: 400;
    line-height: 1;
    text-transform: uppercase;
  }
  .contact {
    position: absolute;
    left: 0;
    right: 0;
    top: 356px;
    margin: 0;
    text-align: center;
    font-style: normal;
    font-size: 22px;
    line-height: 29px;
    letter-spacing: 4px;
  }
  .contact span { display: block; }
</style>
</head>
<body>
  <main class="card">
    <h1 class="company-name">Quill Harbour</h1>
    <p class="person-name">Melda Porrins</p>
    <address class="contact">
      <span class="contact-postal">PO Box 572 Tallowfern Qld 4391</span>
      <span class="contact-digital">melda@quillharbour.com.au 0427 861593</span>
    </address>
  </main>
</body>
</html>
```